I’d like to see something with similar colors and design concept to the “Your Fortune Starts at Breakfast” book included in attchment

Create a book cover with front cover, and full front, spine and back cover spread.
Simple and clean design. See design inspiration below.
Size 6X9
Title of the book: Write Onward! Veteran Editors Reveal Their Methods

Please leave space for 6 authors names on the front cover. Authors names will be provided at a later time.

Back of book should included the name of the publishing company:
Bright Lantern Publishing

As well as the following synopsis
The landscape of the publishing industry is changing. Gone are the days of coveted gatekeepers controlling content and dictating the messages being distributed. With the rise of technology, social media , self-publishing platforms, and independent bookstores, there are increased opportunities for people to share their ideas, messages, and stories with the world through books. The types of books that we’re publishing are also evolving — mini-books, audio books, journals, multi-author books, cook books, children’s books, comic books, coloring books, interactive books, tarot and oracle card decks are all expanding the podium for people to express ideas and influence the culture. More and more entrepreneurs are posturing themselves as thought leaders by leveraging this growing platform.
But that doesn't mean it’s easy.
Even with the expanding platforms and opportunities, only a fraction of people with publishing ambitions are able to achieve this coveted dream held by so many. It can be a daunting process for budding authors trying to maneuver through the writing, packaging, marketing, and publishing processes alone.

In this book you'll find passionate, purpose-driven, and well-versed experts working in the various areas of publishing, eager to help open your eyes to the promise of publishing and effortlessly guide you through the process.

Colors
0094D4
00A9DD
6FCCEA
C7EBF8
E9F6FB
FFF300
FFF600
FEFA6F
FFFEC7
FFFEE8
FFC000
F8CF3A
FAE287
FDF2CF
FEFAEE
F0912C
F2A743
F7CA91
FBE8D2
FDF5EE
EE7325
F08F49
F5BC92
FAE3D3
FDF4ED
6B429C
8869AF
B7A5CE
E3DAEB
F3F0F8

```html
<!DOCTYPE html>
<html lang="en">
<head>
<meta charset="utf-8">
<title>Write Onward! Veteran Editors Reveal Their Methods — Cover Spread</title>
<link rel="stylesheet" href="https://fonts.googleapis.com/css2?family=Bebas+Neue&family=Roboto+Condensed:wght@400;700&display=swap">
<style>
  :root {
    --stage: #333333;
    --cream: #eeebe0;
    --red: #e63323;
    --gold: #c3a95a;
    --gold-soft: #d6c68f;
    --ink: #111111;
    --keyhole: #0e1024;
    --white: #ffffff;
    --barcode-line: #e8a090;
  }
  * { margin: 0; padding: 0; box-sizing: border-box; }
  html, body { width: 1200px; height: 1177px; overflow: hidden; }
  body { background: var(--stage); position: relative; font-family: "Roboto Condensed", sans-serif; }

  .panel { position: absolute; top: 218px; height: 706px; background: var(--cream); overflow: hidden; }
  .back-cover { left: 91px; width: 471px; }
  .spine { left: 566px; width: 75px; }
  .front-cover { left: 644px; width: 468px; }

  .red-field { position: absolute; inset: 0; width: 100%; height: 100%; }
  .red-field polygon { fill: var(--red); }

  .display { font-family: "Bebas Neue", sans-serif; font-weight: 400; line-height: 1; }

  /* Back cover */
  .back-title { position: absolute; left: 37px; top: 20px; color: var(--white); font-size: 86px; line-height: 70px; }
  .back-subtitle { position: absolute; left: 37px; top: 160px; color: var(--white); font-size: 32px; white-space: nowrap; }
  .back-key { position: absolute; left: 292px; top: 203px; width: 102px; height: 30px; border-radius: 15px 4px 4px 15px; background: linear-gradient(90deg, var(--gold) 0%, var(--gold-soft) 100%); }
  .back-keyhole { position: absolute; left: 405px; top: 210px; width: 32px; height: 74px; border-radius: 16px 16px 3px 3px; background: var(--keyhole); }
  .synopsis { position: absolute; left: 27px; top: 356px; width: 418px; font-size: 11.2px; line-height: 14.3px; color: var(--ink); text-align: justify; }
  .synopsis p + p { margin-top: 14px; }
  .synopsis .closing { font-weight: 700; }
  .back-publisher { position: absolute; left: 20px; top: 673px; font-size: 13px; color: var(--ink); }
  .barcode-space { position: absolute; left: 321px; top: 648px; width: 126px; height: 44px; border: 1px solid var(--barcode-line); background: var(--white); display: flex; align-items: center; justify-content: center; font-size: 11px; color: var(--ink); }

  /* Spine */
  .spine-title { position: absolute; left: 0; top: 26px; width: 75px; writing-mode: vertical-rl; color: var(--white); font-size: 53px; display: flex; align-items: center; white-space: nowrap; }
  .spine-subtitle { position: absolute; left: 0; top: 356px; width: 75px; writing-mode: vertical-rl; color: var(--ink); font-size: 21px; display: flex; align-items: center; white-space: nowrap; }
  .spine-publisher { position: absolute; left: 0; bottom: 12px; width: 75px; text-align: center; font-size: 10.5px; line-height: 12px; color: var(--ink); }

  /* Front cover */
  .front-publisher { position: absolute; right: 14px; top: 14px; text-align: right; color: var(--white); font-size: 16px; line-height: 20px; }
  .author-list { position: absolute; left: 19px; top: 13px; list-style: none; }
  .author-slot { position: relative; width: 150px; height: 59px; }
  .author-name { position: absolute; left: 61px; top: -2px; font-size: 12.5px; color: var(--ink); letter-spacing: 0.2px; }
  .author-key { position: absolute; left: 0; top: 18px; width: 146px; height: 38px; border-radius: 19px 4px 4px 19px; background: linear-gradient(90deg, var(--gold) 0%, var(--gold-soft) 100%); }
  .front-keyhole { position: absolute; left: 380px; top: 183px; width: 44px; height: 95px; border-radius: 22px 22px 4px 4px; background: var(--keyhole); }
  .lone-figure { position: absolute; left: 155px; top: 452px; width: 111px; height: 77px; background: linear-gradient(100deg, rgba(20,20,20,0.45) 0%, rgba(20,20,20,0.18) 45%, rgba(238,235,224,0) 100%); }
  .front-title { position: absolute; left: 20px; top: 574px; font-size: 90px; white-space: nowrap; color: var(--ink); }
  .front-title .accent { color: var(--red); }
  .title-rule { position: absolute; left: 20px; top: 650px; width: 425px; height: 2px; background: var(--red); }
  .front-subtitle { position: absolute; left: 20px; top: 655px; font-size: 32px; color: var(--ink); white-space: nowrap; }
</style>
</head>
<body>

<section class="panel back-cover" aria-label="Back cover">
  <svg class="red-field" viewBox="0 0 471 706" preserveAspectRatio="none" aria-hidden="true"><polygon points="0,0 471,0 471,320 0,211"/></svg>
  <h2 class="display back-title">Write<br>Onward</h2>
  <p class="display back-subtitle">Veteran Editors Reveal Their Methods</p>
  <div class="back-key" role="img" aria-label="Gold key illustration"></div>
  <div class="back-keyhole" role="img" aria-label="Keyhole illustration"></div>
  <div class="synopsis">
    <p>The landscape of the publishing industry is changing. Gone are the days of coveted gatekeepers controlling content and dictating the messages being distributed. With the rise of technology, social media , self-publishing platforms, and independent bookstores, there are increased opportunities for people to share their ideas, messages, and stories with the world through books. The types of books that we’re publishing are also evolving — mini-books, audio books, journals, multi-author books, cook books, children’s books, comic books, coloring books, interactive books, tarot and oracle card decks are all expanding the podium for people to express ideas and influence the culture. More and more entrepreneurs are posturing themselves as thought leaders by leveraging this growing platform.</p>
    <p>But that doesn't mean it’s easy.<br>Even with the expanding platforms and opportunities, only a fraction of people with publishing ambitions are able to achieve this coveted dream held by so many. It can be a daunting process for budding authors trying to maneuver through the writing, packaging, marketing, and publishing processes alone.</p>
    <p class="closing">In this book you'll find passionate, purpose-driven, and well-versed experts working in the various areas of publishing, eager to help open your eyes to the promise of publishing and effortlessly guide you through the process.</p>
  </div>
  <p class="back-publisher">Bright Lantern Publishing</p>
  <div class="barcode-space">BARCODE</div>
</section>

<section class="panel spine" aria-label="Spine">
  <svg class="red-field" viewBox="0 0 75 706" preserveAspectRatio="none" aria-hidden="true"><polygon points="0,0 75,0 75,335 0,318"/></svg>
  <p class="display spine-title">Write Onward</p>
  <p class="display spine-subtitle">Veteran Editors Reveal Their Methods</p>
  <p class="spine-publisher">Bright<br>Lantern<br>Publishing</p>
</section>

<section class="panel front-cover" aria-label="Front cover">
  <svg class="red-field" viewBox="0 0 468 706" preserveAspectRatio="none" aria-hidden="true"><polygon points="301,0 468,0 468,440 301,401"/></svg>
  <p class="front-publisher">Bright Lantern<br>Publishing</p>
  <ul class="author-list">
    <li class="author-slot"><span class="author-name">AUTHOR 1</span><div class="author-key" role="img" aria-label="Gold key illustration"></div></li>
    <li class="author-slot"><span class="author-name">AUTHOR 2</span><div class="author-key" role="img" aria-label="Gold key illustration"></div></li>
    <li class="author-slot"><span class="author-name">AUTHOR 3</span><div class="author-key" role="img" aria-label="Gold key illustration"></div></li>
    <li class="author-slot"><span class="author-name">AUTHOR 4</span><div class="author-key" role="img" aria-label="Gold key illustration"></div></li>
    <li class="author-slot"><span class="author-name">AUTHOR 5</span><div class="author-key" role="img" aria-label="Gold key illustration"></div></li>
    <li class="author-slot"><span class="author-name">AUTHOR 6</span><div class="author-key" role="img" aria-label="Gold key illustration"></div></li>
  </ul>
  <div class="front-keyhole" role="img" aria-label="Keyhole illustration in the red wall"></div>
  <div class="lone-figure" role="img" aria-label="Small silhouette of a person standing and casting a long shadow"></div>
  <h1 class="display front-title">Write <span class="accent">Onward</span></h1>
  <div class="title-rule"></div>
  <p class="display front-subtitle">Veteran Editors Reveal Their Methods</p>
</section>

</body>
</html>
```